Business Card Design for a Personal Trainer

I need a business card design for my job as a personal trainer. It should have a unique, modern and exclusive design. On the front there should be only my logo with my name and my job. 0163/2918374 Tobias Kellinger Lindenfeldweg 14 80412 Munich Germany The most important contact information is the web adress. it can be bigger than the rest, but its not necessary. The card should be 8,5cmx5,5cm big. Font: Roboto. Colors: black, white, gray, 56c1ff.

```html
<!DOCTYPE html>
<html lang="de">
<head>
<meta charset="utf-8">
<title>Tobias Kellinger – Business Cards</title>
<link href="https://fonts.googleapis.com/css2?family=Roboto:wght@400;500&display=swap" rel="stylesheet">
<style>
  :root {
    --page: #e6e6e6;
    --card-black: #0d0d0d;
    --card-dark: #1c1c1c;
    --white: #ffffff;
    --gray-text: #d9d9d9;
    --accent: #56c1ff;
    --smoke-light: #cfcfcf;
    --smoke-mid: #7a7a7a;
  }
  * { margin: 0; padding: 0; box-sizing: border-box; }
  html, body {
    width: 1200px; height: 1200px; overflow: hidden;
    background: var(--page);
    font-family: "Roboto", Arial, sans-serif;
  }
  .card {
    position: absolute;
    left: 226px;
    width: 749px;
    height: 415px;
    overflow: hidden;
    background:
      radial-gradient(ellipse at 30% 30%, rgba(60,60,60,0.35), transparent 60%),
      radial-gradient(ellipse at 85% 90%, rgba(50,50,50,0.35), transparent 55%),
      var(--card-black);
  }
  .card--front { top: 146px; }
  .card--back { top: 637px; }

  .brand-square {
    position: absolute;
    background: var(--accent);
  }
  .card--front .brand-square { width: 56px; height: 56px; left: 346px; top: 136px; }
  .card--back .brand-square { width: 38px; height: 38px; left: 171px; top: 70px; }

  .wordmark {
    position: absolute;
    color: var(--white);
    text-align: center;
  }
  .wordmark__name {
    font-weight: 400;
    white-space: nowrap;
    line-height: 1;
  }
  .wordmark__role {
    display: flex;
    align-items: center;
    gap: 6px;
    color: var(--gray-text);
    text-transform: uppercase;
    line-height: 1;
  }
  .wordmark__role::before,
  .wordmark__role::after {
    content: "";
    flex: 1;
    height: 1.5px;
    background: var(--gray-text);
  }
  .card--front .wordmark { left: 0; right: 0; top: 242px; display: flex; flex-direction: column; align-items: center; }
  .card--front .wordmark__name { font-size: 47px; letter-spacing: -0.5px; }
  .card--front .wordmark__role { width: 394px; font-size: 17px; letter-spacing: 5.5px; margin-top: 8px; }
  .card--back .wordmark { left: 68px; top: 136px; width: 242px; }
  .card--back .wordmark__name { font-size: 29px; letter-spacing: -0.3px; }
  .card--back .wordmark__role { font-size: 11px; letter-spacing: 3px; margin-top: 5px; }

  .photo-area {
    position: absolute;
    right: 0; top: 0;
    width: 430px; height: 100%;
    background:
      radial-gradient(ellipse at 70% 55%, var(--smoke-light) 0%, var(--smoke-mid) 45%, transparent 75%),
      radial-gradient(ellipse at 40% 20%, rgba(190,190,190,0.7), transparent 55%);
  }

  .contact {
    position: absolute;
    left: 68px; top: 228px;
    color: var(--white);
    font-size: 15.5px;
  }
  .contact__address { margin-bottom: 24px; }
  .contact__list { list-style: none; }
  .contact__item {
    display: flex; align-items: center;
    height: 26px; margin-bottom: 7px;
    font-size: 16px;
  }
  .contact__icon { width: 34px; height: 26px; margin-right: 12px; flex: none; }
</style>
</head>
<body>

<section class="card card--front">
  <div class="brand-square"></div>
  <div class="wordmark">
    <div class="wordmark__name">TOBIAS KELLINGER</div>
    <div class="wordmark__role">Personal Trainer</div>
  </div>
</section>

<section class="card card--back">
  <div class="photo-area" role="img" aria-label="Black and white portrait of the trainer with arms crossed in front of a cloud of chalk dust"></div>
  <div class="brand-square"></div>
  <div class="wordmark">
    <div class="wordmark__name">TOBIAS KELLINGER</div>
    <div class="wordmark__role">Personal Trainer</div>
  </div>
  <div class="contact">
    <p class="contact__address">Lindenfeldweg 14, 80412, München</p>
    <ul class="contact__list">
      <li class="contact__item">
        <svg class="contact__icon" viewBox="0 0 34 26" aria-hidden="true">
          <path d="M0 0H27L34 13L27 26H0Z" fill="var(--accent)"/>
          <path d="M8 17h14v3H8z M10 17l2-6h6l2 6z M7 9c3-3 13-3 16 0v2h-4v-1h-8v1H7z" fill="var(--white)"/>
        </svg>
        0163/2918374
      </li>
      <li class="contact__item">
        <svg class="contact__icon" viewBox="0 0 34 26" aria-hidden="true">
          <path d="M0 0H27L34 13L27 26H0Z" fill="var(--accent)"/>
          <rect x="7" y="7" width="17" height="12" fill="none" stroke="var(--white)" stroke-width="1.6"/>
          <path d="M7 7l8.5 7L24 7" fill="none" stroke="var(--white)" stroke-width="1.6"/>
        </svg>
        t.kellinger@postmail.de
      </li>
      <li class="contact__item">
        <svg class="contact__icon" viewBox="0 0 34 26" aria-hidden="true">
          <path d="M0 0H27L34 13L27 26H0Z" fill="var(--accent)"/>
          <rect x="7" y="6" width="17" height="11" fill="none" stroke="var(--white)" stroke-width="1.8"/>
          <path d="M13 20h5M15.5 17v3" stroke="var(--white)" stroke-width="1.8"/>
        </svg>
        www.tobiaskellinger.de
      </li>
    </ul>
  </div>
</section>

</body>
</html>
```